party concept called Marejada.*

I need key art made for a new party concept called Marejada.

Marejada is a monthly latin dance party playing the best of BACHATA music. Bachata is a genre of Latin America music that originated in the Dominican Republic in the first half of the 20th century with Indigenous, African and European musical elements.

Our demographic is generally upscale, 25 - 45 yrs old that loves to party, dance, and have a good time. We want the flyer to have to have a tropical vibe that is bright and fun.

Fun fact, Bachata music originated from brothels— so it has a very sexy origin. Would love for the key art to have a sexy flair to it as well.

In terms of sizes, we will need a flyer made in the following sizes:
1080x1350
1080x1080
2160 x 1080
1080x1920

*I will need the final graphics in BOTH a LAYERED PSD file and JPG.

We are just hoping for a fun, colorful key art flyer that will get people excited to attend the party.

Sample Text:
MAREJADA
FRIDAY MARCH 13
10 PM - 2 AM
Kirchbühlgasse 21
...

please post more designs ideas with brown color Regards

Font styles to use
Sans Serif
Decorative

Colors
ff2c1d
ff5442

```html
<!DOCTYPE html>
<html lang="en">
<head>
<meta charset="utf-8">
<title>Marejada Bachata – Flyer Set</title>
<link rel="stylesheet" href="https://fonts.googleapis.com/css2?family=Anton&family=Oswald:wght@500;700&family=Montserrat:wght@600;800&family=Kaushan+Script&display=block">
<style>
  :root{
    --red:#ff2c1d;
    --red-light:#ff5442;
    --red-deep:#b3140b;
    --salmon:#f08a6e;
    --peach:#f6c2ae;
    --cream:#fbefe9;
    --brown:#5a2a1f;
    --palm:#c65a44;
    --conga:#b8654c;
    --skin:#e2a58e;
    --ink:#2a1510;
    --stage:#e4e4e4;
  }
  *{margin:0;padding:0;box-sizing:border-box}
  html,body{width:1200px;height:800px;overflow:hidden}
  body{background:var(--stage);position:relative;font-family:"Montserrat",sans-serif;color:var(--ink)}

  .flyer{position:absolute;overflow:hidden;box-shadow:0 6px 14px rgba(0,0,0,.25);
    background:
      radial-gradient(ellipse at 50% 100%, rgba(255,84,66,.45), transparent 55%),
      linear-gradient(180deg,var(--cream),#f6e4dc 55%,#f4cdbd);}
  .flyer--banner{left:88px;top:55px;width:552px;height:288px}
  .flyer--square{left:220px;top:433px;width:255px;height:287px}
  .flyer--portrait{left:712px;top:172px;width:403px;height:528px}

  /* artwork placeholders */
  .art{position:absolute}
  .art--palm{background:radial-gradient(ellipse at 50% 40%, rgba(198,90,68,.75) 0%, rgba(214,120,96,.45) 45%, transparent 72%)}
  .art--conga{border-radius:40% 40% 30% 30%/20% 20% 12% 12%;
    background:linear-gradient(90deg,#a24d37,var(--conga) 35%,#e29a80 60%,#9c4732)}
  .art--dancer{background:radial-gradient(ellipse at 50% 45%, var(--skin) 0%, #d98a72 45%, rgba(217,138,114,.4) 70%, transparent 82%)}
  .art--smoke{background:radial-gradient(ellipse at 50% 80%, rgba(255,110,90,.65), rgba(255,140,120,.3) 50%, transparent 75%)}

  .tagline{position:absolute;left:0;right:0;text-align:center;font-family:"Oswald",sans-serif;
    font-weight:500;color:var(--brown);letter-spacing:.28em;text-transform:uppercase;z-index:2}
  .info{position:absolute;text-align:center;z-index:2}
  .title{font-family:"Oswald",sans-serif;font-weight:700;color:var(--red);line-height:1;letter-spacing:.01em;
    text-shadow:0 2px 0 var(--red-deep),0 4px 6px rgba(0,0,0,.3)}
  .subtitle{font-family:"Kaushan Script",cursive;color:var(--red-light);display:block;line-height:1;position:relative;
    transform:rotate(-10deg);text-shadow:0 0 2px #fff,0 0 3px #fff,0 0 4px #fff,0 2px 4px rgba(0,0,0,.3)}
  .date{font-weight:800;color:var(--ink);letter-spacing:.03em}
  .time{display:inline-block;font-weight:800;color:var(--ink);border:2px solid var(--salmon);
    border-radius:5px;background:rgba(255,255,255,.75)}
  .address{font-weight:600;color:var(--ink);letter-spacing:.08em}
  .contact{font-weight:600;color:var(--ink);text-transform:uppercase}

  /* banner */
  .flyer--banner .tagline{top:20px;font-size:11px}
  .flyer--banner .info{left:235px;width:310px;top:58px}
  .flyer--banner .title{font-size:72px}
  .flyer--banner .subtitle{font-size:34px;margin:-22px 0 0 40px;text-align:center}
  .flyer--banner .date{font-size:20px;margin-top:4px}
  .flyer--banner .time{font-size:14px;padding:1px 10px;margin-top:4px}
  .flyer--banner .address{font-size:11px;margin-top:6px}
  .flyer--banner .contact{font-size:7px;margin-top:20px;white-space:nowrap}

  /* square */
  .flyer--square .tagline{top:7px;font-size:7px}
  .flyer--square .info{left:0;right:0;top:136px}
  .flyer--square .title{font-size:52px}
  .flyer--square .subtitle{font-size:24px;margin:-16px 0 0 30px}
  .flyer--square .date{font-size:13px;margin-top:6px}
  .flyer--square .time{font-size:10px;padding:0 8px;margin-top:4px}
  .flyer--square .address{font-size:8px;margin-top:5px}
  .flyer--square .contact{font-size:5px;margin-top:3px;white-space:nowrap}

  /* portrait */
  .flyer--portrait .tagline{top:26px;font-size:11px}
  .flyer--portrait .info{left:0;right:0;top:240px}
  .flyer--portrait .title{font-size:88px}
  .flyer--portrait .subtitle{font-size:42px;margin:-26px 0 0 70px}
  .flyer--portrait .date{font-size:23px;margin-top:8px}
  .flyer--portrait .time{font-size:17px;padding:1px 12px;margin-top:8px}
  .flyer--portrait .address{font-size:13px;margin-top:8px}
  .flyer--portrait .contact{font-size:7.5px;margin-top:12px;white-space:nowrap}
</style>
</head>
<body>

<section class="flyer flyer--banner" aria-label="Marejada Bachata banner 2160x1080">
  <div class="art art--palm" style="left:-10px;top:-10px;width:110px;height:150px" role="img" aria-label="Palm fronds, left corner"></div>
  <div class="art art--palm" style="left:210px;top:10px;width:140px;height:160px" role="img" aria-label="Palm tree behind the dancer"></div>
  <div class="art art--palm" style="left:490px;top:-10px;width:80px;height:120px" role="img" aria-label="Palm fronds, right corner"></div>
  <div class="art art--conga" style="left:20px;top:100px;width:80px;height:190px" role="img" aria-label="Conga drum"></div>
  <div class="art art--conga" style="left:210px;top:115px;width:60px;height:170px" role="img" aria-label="Conga drum"></div>
  <div class="art art--dancer" style="left:85px;top:25px;width:200px;height:263px" role="img" aria-label="Photo of a seated woman in a white top"></div>
  <div class="art art--smoke" style="left:0;top:200px;width:300px;height:120px" role="img" aria-label="Soft coral smoke"></div>
  <p class="tagline">Playing the best of Bachata music</p>
  <div class="info">
    <h1 class="title">MAREJADA</h1>
    <span class="subtitle">Bachata</span>
    <p class="date">FRIDAY MARCH 13</p>
    <span class="time">10 PM - 2 AM</span>
    <p class="address">Kirchbühlgasse 21</p>
    <p class="contact">For more info about event call us at +00 987 654 3210</p>
  </div>
</section>

<section class="flyer flyer--square" aria-label="Marejada Bachata square flyer 1080x1080">
  <div class="art art--palm" style="left:-10px;top:10px;width:70px;height:110px" role="img" aria-label="Palm fronds, left"></div>
  <div class="art art--palm" style="left:165px;top:5px;width:100px;height:130px" role="img" aria-label="Palm tree, right"></div>
  <div class="art art--conga" style="left:28px;top:50px;width:70px;height:130px" role="img" aria-label="Conga drum"></div>
  <div class="art art--conga" style="left:180px;top:60px;width:65px;height:120px" role="img" aria-label="Conga drum"></div>
  <div class="art art--dancer" style="left:80px;top:15px;width:115px;height:170px" role="img" aria-label="Photo of a seated woman in a white top"></div>
  <div class="art art--smoke" style="left:0;top:170px;width:255px;height:120px" role="img" aria-label="Soft coral smoke"></div>
  <p class="tagline">Playing the best of Bachata music</p>
  <div class="info">
    <h2 class="title">MAREJADA</h2>
    <span class="subtitle">Bachata</span>
    <p class="date">FRIDAY MARCH 13</p>
    <span class="time">10 PM - 2 AM</span>
    <p class="address">Kirchbühlgasse 21</p>
    <p class="contact">For more info about event call us at +00 987 654 3210</p>
  </div>
</section>

<section class="flyer flyer--portrait" aria-label="Marejada Bachata portrait flyer 1080x1350">
  <div class="art art--palm" style="left:-10px;top:10px;width:110px;height:160px" role="img" aria-label="Palm fronds, left"></div>
  <div class="art art--palm" style="left:235px;top:25px;width:170px;height:190px" role="img" aria-label="Palm tree, right"></div>
  <div class="art art--conga" style="left:32px;top:118px;width:88px;height:180px" role="img" aria-label="Conga drum"></div>
  <div class="art art--conga" style="left:265px;top:163px;width:105px;height:160px" role="img" aria-label="Conga drum"></div>
  <div class="art art--dancer" style="left:105px;top:50px;width:190px;height:290px" role="img" aria-label="Photo of a seated woman in a white top"></div>
  <div class="art art--smoke" style="left:0;top:320px;width:403px;height:210px" role="img" aria-label="Soft coral smoke"></div>
  <p class="tagline">Playing the best of Bachata music</p>
  <div class="info">
    <h2 class="title">MAREJADA</h2>
    <span class="subtitle">Bachata</span>
    <p class="date">FRIDAY MARCH 13</p>
    <span class="time">10 PM - 2 AM</span>
    <p class="address">Kirchbühlgasse 21</p>
    <p class="contact">For more info about event call us at +00 987 654 3210</p>
  </div>
</section>

</body>
</html>
```